Verdalunex webpage design

We are offering eco/sustainable theme vacations and make them bookable via our site. Our reference site is www.hovkalume.com. We want something similar but with a bit more creativity and elegant design. In our colors, which would depend on our logo colors.

NB: WE ARE NOT ASKING FOR A FULL BLOWN SITE. WE NEED 2 PAGE DESIGN FOR THE FIRST IMPRESSION. AFTER THAT WE CREATE A BUDGET FOR COMPLETION OF THE PROJECT.

Target Market(s)

Eco/Sustainable tourism.

Industry/Entity Type

Tourism

Coding

Coded - Design and coding required

Number of Pages Required

2 page

Requirements
Must have
• Reference site is hovkalume.com. But be creative and design something a bit different and more beautiful.
• NB: WE ARE NOT ASKING FOR A FULL BLOWN SITE. WE NEED 2 PAGE DESIGN FOR THE FIRST IMPRESSION. AFTER THAT WE CREATE A BUDGET FOR COMPLETION OF THE PROJECT.
• Please see our logo.

```html
<!DOCTYPE html>
<html lang="en">
<head>
<meta charset="utf-8">
<title>Verdalunex – Memorable Travel Experience</title>
<link href="https://fonts.googleapis.com/css2?family=Open+Sans:wght@400;600;700;800&display=swap" rel="stylesheet">
<style>
:root{
  --mint:#7fd6b8;
  --mint-dark:#4cc29a;
  --green:#2fbf86;
  --blue:#2b9af3;
  --ink:#2d2d2d;
  --muted:#777;
  --line:#dcdcdc;
  --panel:#f2f2f2;
  --star:#f5b301;
  --orange:#f7941d;
  --white:#fff;
}
*{box-sizing:border-box;margin:0;padding:0}
html,body{width:1200px;height:4344px;overflow:hidden}
body{font-family:"Open Sans",Arial,sans-serif;color:var(--ink);background:var(--white);position:relative}
ul{list-style:none}

/* hero */
.hero{position:absolute;left:0;top:0;width:1200px;height:768px;
  background:linear-gradient(180deg,#8fa9bf 0%,#c8d3dc 30%,#e9ecee 55%,#8aa4b6 75%,#1f4d6b 100%)}
.nav{position:absolute;left:0;top:0;width:100%;height:110px;display:flex;align-items:center;justify-content:space-between;padding:0 40px;background:linear-gradient(180deg,rgba(0,0,0,.35),rgba(0,0,0,0))}
.brand{display:flex;align-items:center;gap:12px;color:var(--white);font-size:40px;font-weight:600;letter-spacing:.5px}
.brand-dot{width:22px;height:22px;border-radius:50%;background:var(--mint)}
.nav-links{display:flex;align-items:center;gap:34px;color:var(--white);font-size:17px;font-weight:600}
.nav-links .signup{background:var(--mint-dark);padding:6px 14px;border-radius:3px}
.hero-title{position:absolute;top:318px;width:100%;text-align:center;color:var(--white);font-size:52px;font-weight:800;text-shadow:0 2px 8px rgba(0,0,0,.35)}
.hero-sub{position:absolute;top:392px;width:100%;text-align:center;color:var(--white);font-size:20px;font-weight:600;text-shadow:0 1px 6px rgba(0,0,0,.4)}
.search{position:absolute;left:120px;top:448px;width:960px;height:96px;background:var(--white);border-radius:4px;display:flex;align-items:center;padding:0 16px;box-shadow:0 4px 14px rgba(0,0,0,.2)}
.search-field{flex:1;display:flex;align-items:center;gap:14px;padding:0 18px;border-right:1px solid var(--line);height:56px}
.search-field:nth-child(3){border-right:none}
.search-field svg{flex:none}
.search-field b{display:block;font-size:13px;font-weight:700;letter-spacing:.3px}
.search-field span{font-size:20px;color:#555}
.search-btn{width:72px;height:64px;background:var(--mint-dark);border-radius:4px;display:flex;align-items:center;justify-content:center}

/* stats */
.stats{position:absolute;left:0;top:768px;width:1200px;height:212px;background:var(--mint);display:flex;justify-content:space-around;align-items:center;padding:0 60px;color:var(--white);text-align:center}
.stat strong{display:block;font-size:60px;font-weight:800;line-height:1.1}
.stat span{font-size:22px;font-weight:600}

/* sidebar */
.sidebar{position:absolute;left:64px;top:1000px;width:320px}
.filter{border:1px solid var(--line);margin-bottom:40px;background:var(--white)}
.filter-head{display:flex;align-items:center;gap:14px;height:60px;padding:0 16px;background:var(--panel);font-size:18px;font-weight:700;border-bottom:1px solid var(--line)}
.filter-body{padding:16px 18px 18px}
.select{display:flex;justify-content:space-between;align-items:center;height:52px;font-size:15px;border-bottom:1px solid #eee}
.select.tall{height:64px}
.select:last-child{border-bottom:none}
.select::after{content:"";border:7px solid transparent;border-top:8px solid #222;margin-top:8px}
.option{display:flex;align-items:center;gap:10px;font-size:15px;height:36px}
.option i{width:15px;height:15px;border:1.5px solid #888;border-radius:50%;flex:none}
.option i.box{border-radius:2px}
.more{color:var(--blue);font-size:15px;font-weight:600;padding:4px 0 0 25px}

/* listings */
.listings{position:absolute;left:488px;top:1000px;width:672px}
.sort{font-size:15px;height:48px;display:flex;align-items:center;gap:8px}
.sort b{font-weight:700}
.card{height:396px;margin-top:12px;margin-bottom:28px;border:1px solid var(--line);background:var(--white);display:flex;flex-direction:column}
.card-title{height:56px;background:var(--blue);color:var(--white);font-size:19px;font-weight:700;display:flex;align-items:center;justify-content:space-between;padding:0 20px}
.card-body{flex:1;display:flex;gap:28px;padding:24px}
.card-photo{width:200px;height:224px;flex:none}
.card-info{font-size:16px;padding-top:6px}
.stars{display:flex;align-items:center;gap:3px;color:var(--muted);font-size:15px}
.from{margin-top:12px;font-size:15px;color:var(--muted)}
.price{font-size:30px;font-weight:700;color:#333;line-height:1.1}
.meta{display:flex;align-items:center;gap:10px;margin-top:10px;font-size:16px}
.card-foot{height:64px;background:var(--panel);display:flex;align-items:center;padding-left:24px;position:relative}
.feature{display:flex;align-items:center;gap:8px;font-size:13px;line-height:1.2;width:150px;color:#555}
.details{position:absolute;right:0;top:0;height:64px;width:190px;background:var(--green);color:var(--white);font-weight:700;font-size:18px;display:flex;align-items:center;justify-content:center;padding-left:30px;clip-path:polygon(30px 0,100% 0,100% 100%,0 100%)}
.load{width:176px;height:48px;margin:0 auto;background:var(--orange);color:var(--white);font-weight:700;font-size:17px;display:flex;align-items:center;justify-content:center;gap:8px;border-radius:3px}

/* reviews */
.reviews{position:absolute;left:0;top:3330px;width:1200px;height:410px;background:#f5f5f5;text-align:center}
.reviews h2{font-size:34px;font-weight:700;margin-top:80px}
.reviews .rating{font-size:15px;color:#555;margin-top:4px}
.review-row{display:flex;justify-content:center;gap:60px;margin-top:34px;position:relative}
.review{display:flex;gap:22px;text-align:left;width:460px}
.avatar{width:100px;height:100px;border-radius:50%;background:linear-gradient(135deg,#e9c8ae,#b98b6d);flex:none}
.review .stars{font-size:13px}
.review h3{font-size:17px;color:var(--green);margin:6px 0 4px}
.review p{font-size:14px;color:#666;line-height:1.45}
.review .who{margin-top:8px;font-size:14px;color:#333;font-weight:600}
.review .who span{display:block;font-weight:400;color:#777}
.arrow{position:absolute;top:40px;font-size:30px;color:#444}

/* footer */
.footer{position:absolute;left:0;top:3740px;width:1200px;height:604px;background:var(--mint);color:var(--white)}
.footer .brand{justify-content:center;margin-top:90px;font-size:48px}
.foot-cols{display:flex;justify-content:space-between;padding:0 64px;margin-top:90px}
.foot-col h4{font-size:14px;font-weight:800;letter-spacing:.5px;margin-bottom:12px}
.foot-col li{font-size:13px;line-height:1.7;display:flex;align-items:center;gap:8px}
.dot{width:14px;height:14px;border-radius:50%;background:var(--white);flex:none;opacity:.9}
.newsletter{display:flex}
.newsletter span{width:180px;height:34px;background:var(--white);color:#999;font-size:13px;display:flex;align-items:center;padding-left:10px}
.newsletter b{height:34px;padding:0 14px;background:#333;color:var(--white);font-size:13px;display:flex;align-items:center}
.copyright{position:absolute;bottom:0;width:100%;height:44px;background:var(--mint-dark);font-size:12px;display:flex;align-items:center;justify-content:center;letter-spacing:.5px}
</style>
</head>
<body>

<header class="hero" role="img" aria-label="Photo of white hillside village above a blue sea">
  <nav class="nav">
    <div class="brand"><span class="brand-dot"></span>Verdalunex</div>
    <div class="nav-links">
      <span>US$</span><span>♡ Favorites (0)</span><span>Partners</span><span>Log In</span><span class="signup">Sign Up</span>
    </div>
  </nav>
  <h1 class="hero-title">Memorable Travel Experience</h1>
  <p class="hero-sub">Unique holidays, organized by passionate experts</p>
  <div class="search">
    <div class="search-field">
      <svg width="26" height="30" viewBox="0 0 26 30"><path d="M13 2a9 9 0 0 1 9 9c0 7-9 17-9 17S4 18 4 11a9 9 0 0 1 9-9z" fill="none" stroke="#4aa3df" stroke-width="2.5"/><circle cx="13" cy="11" r="3.5" fill="#4aa3df"/></svg>
      <div><b>DESTINATION</b><span>Any Destination</span></div>
    </div>
    <div class="search-field">
      <svg width="28" height="28" viewBox="0 0 28 28"><rect x="3" y="5" width="22" height="20" rx="2" fill="none" stroke="#4aa3df" stroke-width="2.5"/><path d="M3 11h22M9 2v6M19 2v6" stroke="#4aa3df" stroke-width="2.5"/></svg>
      <div><b>DURATION AND ARRIVAL</b><span>Select Date</span></div>
    </div>
    <div class="search-field">
      <svg width="28" height="28" viewBox="0 0 28 28"><path d="M14 2l3.6 7.6 8.2 1-6 5.7 1.6 8.2L14 20.5 6.6 24.5l1.6-8.2-6-5.7 8.2-1z" fill="none" stroke="#4aa3df" stroke-width="2.2"/></svg>
      <div><b>ACTIVITY TYPE</b><span>Any Category</span></div>
    </div>
    <div class="search-btn"><svg width="32" height="32" viewBox="0 0 32 32"><circle cx="13" cy="13" r="9" fill="none" stroke="#222" stroke-width="3.5"/><path d="M20 20l9 9" stroke="#222" stroke-width="4"/></svg></div>
  </div>
</header>

<section class="stats">
  <div class="stat"><strong>300+</strong><span>Verdalunexers</span></div>
  <div class="stat"><strong>15,000+</strong><span>Travel Packages</span></div>
  <div class="stat"><strong>500,000+</strong><span>Customers per Month</span></div>
</section>

<aside class="sidebar">
  <div class="filter">
    <div class="filter-head"><svg width="22" height="18" viewBox="0 0 22 18"><path d="M1 9h20M13 2l8 7-8 7" fill="none" stroke="#333" stroke-width="2.5"/></svg>Destinations</div>
    <div class="filter-body">
      <div class="select tall">Europe</div><div class="select tall">Asia &amp; Oceania</div><div class="select tall">Africa &amp; Middle East</div><div class="select tall">The Americas &amp; Caribbean</div>
    </div>
  </div>
  <div class="filter">
    <div class="filter-head"><svg width="20" height="20" viewBox="0 0 20 20"><rect x="1" y="3" width="18" height="16" fill="#333"/><rect x="3" y="8" width="14" height="9" fill="#fff"/></svg>Arrival Date</div>
    <div class="filter-body">
      <div class="option"><i></i>2019 May (10234)</div><div class="option"><i></i>2019 June (11366)</div><div class="option"><i></i>2019 July (10618)</div><div class="option"><i></i>2019 August (10323)</div><div class="option"><i></i>2019 September (10626)</div>
      <div class="more">show more</div>
    </div>
  </div>
  <div class="filter">
    <div class="filter-head"><svg width="20" height="20" viewBox="0 0 20 20"><circle cx="10" cy="10" r="8" fill="none" stroke="#333" stroke-width="2.5"/><path d="M10 5v5l3 3" stroke="#333" stroke-width="2.5" fill="none"/></svg>Duration</div>
    <div class="filter-body">
      <div class="option"><i></i>2 days (793)</div><div class="option"><i></i>From 3 to 7 days (8599)</div><div class="option"><i></i>From 1 to 2 weeks (7106)</div><div class="option"><i></i>More than 2 weeks (1890)</div>
    </div>
  </div>
  <div class="filter">
    <div class="filter-head"><svg width="22" height="20" viewBox="0 0 22 20"><path d="M2 11l18-8-5 16-4-6z" fill="#333"/></svg>Airport Transfer</div>
    <div class="filter-body">
      <div class="option"><i class="box"></i>Airport transfer included (5153)</div><div class="option"><i class="box"></i>Airport transfer available (2793)</div>
    </div>
  </div>
  <div class="filter">
    <div class="filter-head"><svg width="20" height="20" viewBox="0 0 20 20"><rect x="1" y="1" width="8" height="8" fill="#333"/><rect x="11" y="1" width="8" height="8" fill="#333"/><rect x="1" y="11" width="8" height="8" fill="#333"/><rect x="11" y="11" width="8" height="8" fill="#333"/></svg>Categories</div>
    <div class="filter-body">
      <div class="select">Accommodation Type</div><div class="select">Activity</div><div class="select">Audience</div><div class="select">Budget</div><div class="select">Duration</div><div class="select">Experience Level</div><div class="select">Experience Type</div><div class="select">Focus/Atmosphere</div><div class="select">Food</div><div class="select">Intensity Level</div><div class="select">Location</div><div class="select">Special Occasion</div><div class="select">Time Periods</div>
    </div>
  </div>
  <div class="filter">
    <div class="filter-head"><svg width="22" height="16" viewBox="0 0 22 16"><rect x="1" y="1" width="20" height="14" rx="2" fill="#333"/><circle cx="11" cy="8" r="3" fill="#fff"/></svg>Price per Trip</div>
    <div class="filter-body">
      <div class="option"><i></i>From US$0 to US$113 (299)</div><div class="option"><i></i>From US$112 to US$337 (1440)</div><div class="option"><i></i>From US$337 to US$1,011 (6598)</div><div class="option"><i></i>More than US$1,011 (8397)</div>
    </div>
  </div>
</aside>

<main class="listings">
  <div class="sort">Sort by : <b>Recommended</b> ▾</div>

  <article class="card">
    <div class="card-title">5 Days Italy by Train Tour in Rome, Florence, Venice<svg width="24" height="22" viewBox="0 0 24 22"><path d="M12 20S2 13 2 7a5 5 0 0 1 10-1 5 5 0 0 1 10 1c0 6-10 13-10 13z" fill="none" stroke="#fff" stroke-width="2.2"/></svg></div>
    <div class="card-body">
      <div class="card-photo" role="img" aria-label="Photo of an ancient stone amphitheatre in Rome" style="background:linear-gradient(180deg,#8fb8e0,#c9a77c 55%,#8d7459)"></div>
      <div class="card-info">
        <div class="stars"><span style="color:var(--star);font-size:20px">★★★★★</span>&nbsp;(3)</div>
        <div class="from">from</div><div class="price">US$1,145</div>
        <div class="meta"><svg width="18" height="18" viewBox="0 0 18 18"><circle cx="9" cy="5" r="4" fill="var(--green)"/><path d="M1 18a8 8 0 0 1 16 0z" fill="var(--green)"/></svg>1 person</div>
        <div class="meta"><svg width="18" height="18" viewBox="0 0 18 18"><rect x="1" y="3" width="16" height="14" rx="1" fill="var(--green)"/><rect x="3" y="7" width="12" height="8" fill="#fff"/></svg>13 days / 12 nights</div>
      </div>
    </div>
    <div class="card-foot">
      <div class="feature"><svg width="20" height="20" viewBox="0 0 20 20"><rect x="2" y="3" width="16" height="15" fill="none" stroke="#666" stroke-width="2"/></svg>Flexible cancellation policy</div>
      <div class="feature"><svg width="20" height="20" viewBox="0 0 20 20"><path d="M2 11l16-8-4 15-4-6z" fill="#666"/></svg>Airport transfer included</div>
      <div class="feature"><svg width="20" height="20" viewBox="0 0 20 20"><path d="M5 2v16M3 2v5h4V2M14 2c-3 3-3 7 0 8v8" fill="none" stroke="#666" stroke-width="2"/></svg>All meals included</div>
      <div class="details">See Details</div>
    </div>
  </article>

  <article class="card">
    <div class="card-title">8 Days Northern Spain Guided Tour in Province of Leon<svg width="24" height="22" viewBox="0 0 24 22"><path d="M12 20S2 13 2 7a5 5 0 0 1 10-1 5 5 0 0 1 10 1c0 6-10 13-10 13z" fill="none" stroke="#fff" stroke-width="2.2"/></svg></div>
    <div class="card-body">
      <div class="card-photo" role="img" aria-label="Photo of a historic stone town at dusk" style="background:linear-gradient(180deg,#6f8fb8,#d9a76c 50%,#7b5b3f)"></div>
      <div class="card-info">
        <div class="stars"><span style="color:var(--star);font-size:20px">★★★★★</span>&nbsp;(3)</div>
        <div class="from">from</div><div class="price">US$1,145</div>
        <div class="meta"><svg width="18" height="18" viewBox="0 0 18 18"><circle cx="9" cy="5" r="4" fill="var(--green)"/><path d="M1 18a8 8 0 0 1 16 0z" fill="var(--green)"/></svg>1 person</div>
        <div class="meta"><svg width="18" height="18" viewBox="0 0 18 18"><rect x="1" y="3" width="16" height="14" rx="1" fill="var(--green)"/><rect x="3" y="7" width="12" height="8" fill="#fff"/></svg>13 days / 12 nights</div>
      </div>
    </div>
    <div class="card-foot">
      <div class="feature"><svg width="20" height="20" viewBox="0 0 20 20"><rect x="2" y="3" width="16" height="15" fill="none" stroke="#666" stroke-width="2"/></svg>Flexible cancellation policy</div>
      <div class="feature"><svg width="20" height="20" viewBox="0 0 20 20"><path d="M2 11l16-8-4 15-4-6z" fill="#666"/></svg>Airport transfer included</div>
      <div class="feature"><svg width="20" height="20" viewBox="0 0 20 20"><path d="M5 2v16M3 2v5h4V2M14 2c-3 3-3 7 0 8v8" fill="none" stroke="#666" stroke-width="2"/></svg>All meals included</div>
      <div class="details">See Details</div>
    </div>
  </article>

  <article class="card">
    <div class="card-title">4 Days Luxury Tour of Madrid, Burgos, and La Rioja in Spain<svg width="24" height="22" viewBox="0 0 24 22"><path d="M12 20S2 13 2 7a5 5 0 0 1 10-1 5 5 0 0 1 10 1c0 6-10 13-10 13z" fill="none" stroke="#fff" stroke-width="2.2"/></svg></div>
    <div class="card-body">
      <div class="card-photo" role="img" aria-label="Photo of a city plaza with a tall building" style="background:linear-gradient(180deg,#9cc3e6,#d7d0c2 55%,#8a8478)"></div>
      <div class="card-info">
        <div class="stars"><span style="color:var(--star);font-size:20px">★★★★★</span>&nbsp;(3)</div>
        <div class="from">from</div><div class="price">US$1,145</div>
        <div class="meta"><svg width="18" height="18" viewBox="0 0 18 18"><circle cx="9" cy="5" r="4" fill="var(--green)"/><path d="M1 18a8 8 0 0 1 16 0z" fill="var(--green)"/></svg>1 person</div>
        <div class="meta"><svg width="18" height="18" viewBox="0 0 18 18"><rect x="1" y="3" width="16" height="14" rx="1" fill="var(--green)"/><rect x="3" y="7" width="12" height="8" fill="#fff"/></svg>13 days / 12 nights</div>
      </div>
    </div>
    <div class="card-foot">
      <div class="feature"><svg width="20" height="20" viewBox="0 0 20 20"><rect x="2" y="3" width="16" height="15" fill="none" stroke="#666" stroke-width="2"/></svg>Flexible cancellation policy</div>
      <div class="feature"><svg width="20" height="20" viewBox="0 0 20 20"><path d="M2 11l16-8-4 15-4-6z" fill="#666"/></svg>Airport transfer included</div>
      <div class="feature"><svg width="20" height="20" viewBox="0 0 20 20"><path d="M5 2v16M3 2v5h4V2M14 2c-3 3-3 7 0 8v8" fill="none" stroke="#666" stroke-width="2"/></svg>All meals included</div>
      <div class="details">See Details</div>
    </div>
  </article>

  <article class="card">
    <div class="card-title">10 Days Guided Sightseeing Tour of Vietnam<svg width="24" height="22" viewBox="0 0 24 22"><path d="M12 20S2 13 2 7a5 5 0 0 1 10-1 5 5 0 0 1 10 1c0 6-10 13-10 13z" fill="none" stroke="#fff" stroke-width="2.2"/></svg></div>
    <div class="card-body">
      <div class="card-photo" role="img" aria-label="Photo of a lantern-lit street in an old town" style="background:linear-gradient(180deg,#c9b24a,#8e9a4c 50%,#5e6a3a)"></div>
      <div class="card-info">
        <div class="stars"><span style="color:var(--star);font-size:20px">★★★★★</span>&nbsp;(3)</div>
        <div class="from">from</div><div class="price">US$1,145</div>
        <div class="meta"><svg width="18" height="18" viewBox="0 0 18 18"><circle cx="9" cy="5" r="4" fill="var(--green)"/><path d="M1 18a8 8 0 0 1 16 0z" fill="var(--green)"/></svg>1 person</div>
        <div class="meta"><svg width="18" height="18" viewBox="0 0 18 18"><rect x="1" y="3" width="16" height="14" rx="1" fill="var(--green)"/><rect x="3" y="7" width="12" height="8" fill="#fff"/></svg>13 days / 12 nights</div>
      </div>
    </div>
    <div class="card-foot">
      <div class="feature"><svg width="20" height="20" viewBox="0 0 20 20"><rect x="2" y="3" width="16" height="15" fill="none" stroke="#666" stroke-width="2"/></svg>Flexible cancellation policy</div>
      <div class="feature"><svg width="20" height="20" viewBox="0 0 20 20"><path d="M2 11l16-8-4 15-4-6z" fill="#666"/></svg>Airport transfer included</div>
      <div class="feature"><svg width="20" height="20" viewBox="0 0 20 20"><path d="M5 2v16M3 2v5h4V2M14 2c-3 3-3 7 0 8v8" fill="none" stroke="#666" stroke-width="2"/></svg>All meals included</div>
      <div class="details">See Details</div>
    </div>
  </article>

  <article class="card">
    <div class="card-title">8 Days Japan<svg width="24" height="22" viewBox="0 0 24 22"><path d="M12 20S2 13 2 7a5 5 0 0 1 10-1 5 5 0 0 1 10 1c0 6-10 13-10 13z" fill="none" stroke="#fff" stroke-width="2.2"/></svg></div>
    <div class="card-body">
      <div class="card-photo" role="img" aria-label="Photo of a pagoda among blossoming trees" style="background:linear-gradient(180deg,#b9d3ec,#e6c6cf 50%,#8a6a5e)"></div>
      <div class="card-info">
        <div class="stars"><span style="color:var(--star);font-size:20px">★★★★★</span>&nbsp;(3)</div>
        <div class="from">from</div><div class="price">US$1,145</div>
        <div class="meta"><svg width="18" height="18" viewBox="0 0 18 18"><circle cx="9" cy="5" r="4" fill="var(--green)"/><path d="M1 18a8 8 0 0 1 16 0z" fill="var(--green)"/></svg>1 person</div>
        <div class="meta"><svg width="18" height="18" viewBox="0 0 18 18"><rect x="1" y="3" width="16" height="14" rx="1" fill="var(--green)"/><rect x="3" y="7" width="12" height="8" fill="#fff"/></svg>13 days / 12 nights</div>
      </div>
    </div>
    <div class="card-foot">
      <div class="feature"><svg width="20" height="20" viewBox="0 0 20 20"><rect x="2" y="3" width="16" height="15" fill="none" stroke="#666" stroke-width="2"/></svg>Flexible cancellation policy</div>
      <div class="feature"><svg width="20" height="20" viewBox="0 0 20 20"><path d="M2 11l16-8-4 15-4-6z" fill="#666"/></svg>Airport transfer included</div>
      <div class="feature"><svg width="20" height="20" viewBox="0 0 20 20"><path d="M5 2v16M3 2v5h4V2M14 2c-3 3-3 7 0 8v8" fill="none" stroke="#666" stroke-width="2"/></svg>All meals included</div>
      <div class="details">See Details</div>
    </div>
  </article>

  <div class="load">⟳ Load More</div>
</main>

<section class="reviews">
  <h2>Reviews from TrustMeadow</h2>
  <p class="rating">Rated 8.7 out of 10 (Good) in 424 reviews</p>
  <div class="review-row">
    <span class="arrow" style="left:64px">‹</span>
    <div class="review">
      <div class="avatar" role="img" aria-label="Reviewer portrait"></div>
      <div>
        <div class="stars"><span style="color:var(--green);font-size:16px">★★★★★</span>&nbsp;Reviewed 2 days ago</div>
        <h3>Well Organized!</h3>
        <p>Lorem ipsum dolor sit amet, consectetur adipiscing elit. Duis faucibus ultricies varius. Proin molestie viverra dolor nec fermentum. Vivamus porttitor tincidunt volutpat.</p>
        <div class="who">Anna Morrell<span>Ancaster, ON</span></div>
      </div>
    </div>
    <div class="review">
      <div class="avatar" role="img" aria-label="Reviewer portrait" style="background:linear-gradient(135deg,#e7c29a,#a97a55)"></div>
      <div>
        <div class="stars"><span style="color:var(--green);font-size:16px">★★★★★</span>&nbsp;Reviewed 2 days ago</div>
        <h3>Well Organized!</h3>
        <p>Lorem ipsum dolor sit amet, consectetur adipiscing elit. Duis faucibus ultricies varius. Proin molestie viverra dolor nec fermentum. Vivamus porttitor tincidunt volutpat.</p>
        <div class="who">Jenna Corwin<span>Ancaster, ON</span></div>
      </div>
    </div>
    <span class="arrow" style="right:64px">›</span>
  </div>
</section>

<footer class="footer">
  <div class="brand"><span class="brand-dot" style="background:#fff"></span>Verdalunex</div>
  <div class="foot-cols">
    <div class="foot-col"><h4>QUICK LINKS</h4><ul><li>Start Something</li><li>Add/Manage Your Business</li><li>Become an Affiliate</li><li>Site Map</li><li>Work With Us</li></ul></div>
    <div class="foot-col"><h4>CONTACT</h4><ul><li><span class="dot"></span>Verdalunex</li><li><span class="dot"></span>12 Groenweg, Utrecht, Netherlands</li><li><span class="dot"></span>0800 123 4567</li><li><span class="dot"></span>info@hovkalume.com</li></ul></div>
    <div class="foot-col"><h4>FOLLOW US</h4><ul><li><span class="dot"></span>Leafline</li><li><span class="dot"></span>Chirpwave</li><li><span class="dot"></span>Snapgrove</li></ul></div>
    <div class="foot-col"><h4>NEWSLETTER</h4><div class="newsletter"><span>Enter email address</span><b>SIGN UP</b></div></div>
  </div>
  <div class="copyright">COPYRIGHT © 2020 VERDALUNEX. ALL RIGHTS RESERVED.</div>
</footer>

</body>
</html>
```